Design for a 4 screens mobile app: Brelluvo

The app is a compact but illustrated phone/address book...
We need a design for the 5 screens of the app (see screens attached):
a) "index" : 1 screen with 6 pictures of contact person
b) "contact list" : 1 screen, to manage (add/del/edit) the contacts of the phone/address book
c) "add contact" : 1 screen to add a contact (a picture + a phone number)
d) "update contact" : similar to "add"
e) "fields missing" : add/edit screens in "error" state
We also need the ico design + loading screen.
No specific guidelines, nor logo or whatever.
It will be a free app distributed on iOS and Androïd.
We just want to make it looking nice & very usable for end users.
B2C

```html
<!DOCTYPE html>
<html lang="en">
<head>
<meta charset="utf-8">
<title>Brelluvo – app screens</title>
<link href="https://fonts.googleapis.com/css2?family=Quicksand:wght@700&family=Roboto:wght@300;400&display=swap" rel="stylesheet">
<style>
  :root{
    --red:#f0443e;
    --red-soft:#f5605a;
    --ink:#333333;
    --muted:#666666;
    --rule:#e2e2e2;
    --paper:#ffffff;
    --canvas:#f4f4f4;
  }
  *{box-sizing:border-box;margin:0;padding:0}
  html,body{width:1200px;height:1200px;overflow:hidden}
  body{background:var(--canvas);position:relative;font-family:'Roboto',sans-serif;color:var(--ink)}

  .screen{position:absolute;width:246px;height:438px;overflow:hidden;
    background:linear-gradient(115deg,#ececec 0%,#f3f3f3 38%,var(--paper) 38.2%,var(--paper) 100%);
    box-shadow:0 6px 18px rgba(0,0,0,.12)}
  .col-1{left:120px}.col-2{left:474px}.col-3{left:833px}
  .row-1{top:105px}.row-2{top:674px}

  .app-title{position:absolute;left:21px;top:24px;font-family:'Quicksand',sans-serif;font-weight:700;font-size:16px;color:var(--red)}
  .app-sub{position:absolute;left:21px;top:45px;font-size:9.5px;color:var(--muted)}
  .top-icon{position:absolute;top:29px;width:20px;height:20px}
  .icon-add{left:169px}.icon-settings{left:203px}.icon-back{left:201px}

  .photo{position:absolute;background:linear-gradient(160deg,#8d9a63,#4c4a3a 70%,#2e2e2e)}
  .photo.tone-green{background:linear-gradient(160deg,#5f8a3c,#2e4f7a 75%)}
  .photo.tone-pale{background:linear-gradient(160deg,#d9d3c4,#3c4a72 80%)}
  .photo.tone-dark{background:linear-gradient(160deg,#5a4a3c,#2e2e30 70%,#3b4f6a)}
  .photo.tone-sun{background:linear-gradient(150deg,#f2c24a,#c28a3a 50%,#5a4a6a)}
  .tile-name{position:absolute;left:7px;bottom:3px;font-family:'Quicksand',sans-serif;font-weight:700;font-size:11px;color:#fff}

  .view-toggle{position:absolute;top:400px;width:22px;height:20px}
  .toggle-grid{left:178px}.toggle-list{left:209px}

  .list-name{position:absolute;left:83px;font-family:'Quicksand',sans-serif;font-weight:700;font-size:11px;color:var(--red)}
  .list-number{position:absolute;left:83px;font-size:11px;color:var(--ink);font-weight:300}

  .splash-photo{position:absolute;inset:0;background:
    radial-gradient(ellipse 60px 170px at 70px 200px,rgba(240,68,62,.85),rgba(240,68,62,0) 100%),
    linear-gradient(135deg,#f6f6f6,#e6e6e6)}
  .splash-name{position:absolute;left:130px;top:160px;font-family:'Quicksand',sans-serif;font-weight:700;font-size:15px;color:var(--red)}

  .drop-zone{position:absolute;left:76px;top:97px;width:100px;height:100px;border:1.2px dashed var(--red);display:flex;align-items:center;justify-content:center}
  .avatar-frame{position:absolute;left:76px;top:97px;width:100px;height:100px;border:1px solid var(--red)}
  .field-name{position:absolute;left:0;right:0;top:224px;text-align:center;font-family:'Quicksand',sans-serif;font-weight:700;font-size:19px;color:var(--red)}
  .field-name .caret{display:inline-block;width:2px;height:19px;background:var(--red);vertical-align:-3px;margin-right:10px}
  .rule{position:absolute;left:0;right:0;height:1px;background:var(--rule)}
  .field-number{position:absolute;left:0;right:0;top:261px;text-align:center;font-size:13px;font-weight:300}
  .btn-save{position:absolute;left:78px;top:350px;width:99px;height:29px;border-radius:7px;background:var(--red);color:#fff;font-size:9.5px;display:flex;align-items:center;justify-content:center}
  .link-delete{position:absolute;left:0;right:0;top:394px;text-align:center;font-size:9.5px;color:var(--ink)}

  .error-overlay{position:absolute;inset:0;background:rgba(245,90,85,.92)}
  .error-message{position:absolute;left:25px;top:186px;font-family:'Quicksand',sans-serif;font-weight:700;font-size:23px;line-height:29px;color:#fff}
  .btn-ok{position:absolute;left:123px;top:298px;width:100px;height:30px;border:1px solid #fff;border-radius:8px;color:#fff;font-size:9px;display:flex;align-items:center;justify-content:center}
</style>
</head>
<body>

<!-- Loading screen -->
<section class="screen col-1 row-1 splash">
  <div class="splash-photo" role="img" aria-label="Photo of a red retro telephone handset with a coiled cord on a light grey surface"></div>
  <div class="splash-name">Brelluvo</div>
</section>

<!-- Index: contact grid -->
<section class="screen col-2 row-1">
  <h1 class="app-title">Brelluvo</h1>
  <p class="app-sub">Your contacts</p>
  <svg class="top-icon icon-add" viewBox="0 0 20 20"><circle cx="10" cy="10" r="9" fill="none" stroke="#f0443e" stroke-width="1.3"/><path d="M10 5v10M5 10h10" stroke="#f0443e" stroke-width="1.3"/></svg>
  <svg class="top-icon icon-settings" viewBox="0 0 20 20"><circle cx="10" cy="10" r="3" fill="none" stroke="#f0443e" stroke-width="1.3"/><path d="M10 1.5l1.6 2.4 2.8-.7.6 2.8 2.7 1-1 2.7 1.6 2.3-2.5 1.4.1 2.9-2.9.1-1.4 2.5-2.3-1.6-2.4 1.6-1.4-2.5-2.9-.1.1-2.9-2.5-1.4 1.6-2.3-1-2.7 2.7-1 .6-2.8 2.8.7z" fill="none" stroke="#f0443e" stroke-width="1.2" stroke-linejoin="round"/></svg>

  <div class="photo" style="left:21px;top:73px;width:99px;height:99px" role="img" aria-label="Portrait photo of Anna"><span class="tile-name">Anna</span></div>
  <div class="photo tone-green" style="left:125px;top:73px;width:99px;height:99px" role="img" aria-label="Portrait photo of Mike"><span class="tile-name">Mike</span></div>
  <div class="photo" style="left:21px;top:178px;width:99px;height:99px" role="img" aria-label="Portrait photo of Janell"><span class="tile-name">Janell</span></div>
  <div class="photo tone-pale" style="left:125px;top:178px;width:99px;height:99px" role="img" aria-label="Portrait photo of Brian"><span class="tile-name">Brian</span></div>
  <div class="photo tone-dark" style="left:21px;top:282px;width:99px;height:99px" role="img" aria-label="Portrait photo of John"><span class="tile-name">John</span></div>
  <div class="photo tone-sun" style="left:125px;top:282px;width:99px;height:99px" role="img" aria-label="Portrait photo of Robert"><span class="tile-name">Robert</span></div>

  <svg class="view-toggle toggle-grid" viewBox="0 0 22 20"><g fill="none" stroke="#f0443e" stroke-width="1.2"><rect x="1" y="2" width="5" height="3.5"/><rect x="8.5" y="2" width="5" height="3.5"/><rect x="16" y="2" width="5" height="3.5"/><rect x="1" y="8" width="5" height="3.5"/><rect x="8.5" y="8" width="5" height="3.5"/><rect x="16" y="8" width="5" height="3.5"/><rect x="1" y="14" width="5" height="3.5"/><rect x="8.5" y="14" width="5" height="3.5"/><rect x="16" y="14" width="5" height="3.5"/></g></svg>
  <svg class="view-toggle toggle-list" viewBox="0 0 22 20"><path d="M1 2h20M1 8h20M1 14h20M1 19h12" stroke="#333" stroke-width="1.2"/></svg>
</section>

<!-- Contact list -->
<section class="screen col-3 row-1">
  <h1 class="app-title">Brelluvo</h1>
  <p class="app-sub">Contact list</p>
  <svg class="top-icon icon-add" viewBox="0 0 20 20"><circle cx="10" cy="10" r="9" fill="none" stroke="#f0443e" stroke-width="1.3"/><path d="M10 5v10M5 10h10" stroke="#f0443e" stroke-width="1.3"/></svg>
  <svg class="top-icon icon-settings" viewBox="0 0 20 20"><circle cx="10" cy="10" r="3" fill="none" stroke="#f0443e" stroke-width="1.3"/><path d="M10 1.5l1.6 2.4 2.8-.7.6 2.8 2.7 1-1 2.7 1.6 2.3-2.5 1.4.1 2.9-2.9.1-1.4 2.5-2.3-1.6-2.4 1.6-1.4-2.5-2.9-.1.1-2.9-2.5-1.4 1.6-2.3-1-2.7 2.7-1 .6-2.8 2.8.7z" fill="none" stroke="#f0443e" stroke-width="1.2" stroke-linejoin="round"/></svg>

  <div class="photo" style="left:22px;top:73px;width:50px;height:50px" role="img" aria-label="Portrait photo of Anna"></div>
  <span class="list-name" style="top:77px">Anna</span><span class="list-number" style="top:91px">555-014-2290</span>
  <div class="photo tone-green" style="left:22px;top:126px;width:50px;height:50px" role="img" aria-label="Portrait photo of Mike"></div>
  <span class="list-name" style="top:131px">Mike</span><span class="list-number" style="top:145px">555-014-2290</span>
  <div class="photo" style="left:22px;top:177px;width:50px;height:50px" role="img" aria-label="Portrait photo of Janell"></div>
  <span class="list-name" style="top:181px">Janell</span><span class="list-number" style="top:195px">555-014-2290</span>
  <div class="photo tone-pale" style="left:22px;top:228px;width:50px;height:50px" role="img" aria-label="Portrait photo of Brian"></div>
  <span class="list-name" style="top:237px">Brian</span><span class="list-number" style="top:251px">555-014-2290</span>
  <div class="photo tone-dark" style="left:22px;top:281px;width:50px;height:50px" role="img" aria-label="Portrait photo of John"></div>
  <span class="list-name" style="top:287px">John</span><span class="list-number" style="top:301px">555-014-2290</span>
  <div class="photo tone-sun" style="left:22px;top:332px;width:50px;height:50px" role="img" aria-label="Portrait photo of Robert"></div>
  <span class="list-name" style="top:342px;font-size:10px">Robert</span><span class="list-number" style="top:356px">555-014-2290</span>

  <svg class="view-toggle toggle-grid" viewBox="0 0 22 20"><g fill="none" stroke="#333" stroke-width="1.2"><rect x="1" y="2" width="5" height="3.5"/><rect x="8.5" y="2" width="5" height="3.5"/><rect x="16" y="2" width="5" height="3.5"/><rect x="1" y="8" width="5" height="3.5"/><rect x="8.5" y="8" width="5" height="3.5"/><rect x="16" y="8" width="5" height="3.5"/><rect x="1" y="14" width="5" height="3.5"/><rect x="8.5" y="14" width="5" height="3.5"/><rect x="16" y="14" width="5" height="3.5"/></g></svg>
  <svg class="view-toggle toggle-list" viewBox="0 0 22 20"><path d="M1 2h20M1 8h20M1 14h20M1 19h12" stroke="#f0443e" stroke-width="1.2"/></svg>
</section>

<!-- Add contact -->
<section class="screen col-1 row-2">
  <h1 class="app-title">Brelluvo</h1>
  <p class="app-sub">Add new contact</p>
  <svg class="top-icon icon-back" viewBox="0 0 20 20"><circle cx="10" cy="10" r="9" fill="none" stroke="#f0443e" stroke-width="1.3"/><path d="M11.5 6l-4 4 4 4" fill="none" stroke="#f0443e" stroke-width="1.3"/></svg>
  <div class="drop-zone">
    <svg width="22" height="24" viewBox="0 0 22 24"><g fill="none" stroke="#f0443e" stroke-width="1.1" stroke-linejoin="round"><path d="M8 22l-4-6c-.6-1 .6-2 1.5-1.2L8 17V7.5a1.2 1.2 0 012.4 0V13l.1-2a1.2 1.2 0 012.4 0v2a1.2 1.2 0 012.4 0v1a1.2 1.2 0 012.4 0v4c0 2-1 4-2 4z"/><path d="M9.2 1v2.5M4.5 3l1.6 1.6M14 3l-1.6 1.6M3 7h2.2"/></g></svg>
  </div>
  <div class="field-name"><span class="caret"></span>Enter name</div>
  <div class="rule" style="top:252px"></div>
  <div class="field-number">| Enter number</div>
  <div class="rule" style="top:285px"></div>
  <div class="btn-save">Save contact</div>
  <div class="link-delete">Delete contact</div>
</section>

<!-- Update contact -->
<section class="screen col-2 row-2">
  <h1 class="app-title">Brelluvo</h1>
  <p class="app-sub">Update contact</p>
  <svg class="top-icon icon-back" viewBox="0 0 20 20"><circle cx="10" cy="10" r="9" fill="none" stroke="#f0443e" stroke-width="1.3"/><path d="M11.5 6l-4 4 4 4" fill="none" stroke="#f0443e" stroke-width="1.3"/></svg>
  <div class="photo avatar-frame" role="img" aria-label="Portrait photo of Anna"></div>
  <div class="field-name">Anna</div>
  <div class="rule" style="top:252px"></div>
  <div class="field-number">555-014-2290</div>
  <div class="rule" style="top:285px"></div>
  <div class="btn-save">Save contact</div>
  <div class="link-delete">Delete contact</div>
</section>

<!-- Fields missing (error state) -->
<section class="screen col-3 row-2">
  <h1 class="app-title">Brelluvo</h1>
  <p class="app-sub">Update contact</p>
  <svg class="top-icon icon-back" viewBox="0 0 20 20"><circle cx="10" cy="10" r="9" fill="none" stroke="#f0443e" stroke-width="1.3"/><path d="M11.5 6l-4 4 4 4" fill="none" stroke="#f0443e" stroke-width="1.3"/></svg>
  <div class="photo avatar-frame" role="img" aria-label="Portrait photo of Anna"></div>
  <div class="rule" style="top:252px"></div>
  <div class="rule" style="top:285px"></div>
  <div class="btn-save">Save contact</div>
  <div class="link-delete">Delete contact</div>
  <div class="error-overlay"></div>
  <p class="error-message">Some fields<br>are missing!</p>
  <div class="btn-ok">OK</div>
</section>

</body>
</html>
```